Quarrow financial services, is a financial company that provides consultancy, brokerage services, and funding.

we will be providing the clients with insights, knowledge and data with regards to the financial markets.

with the brokerage services we will try to find the suitable counterparts that provide them with the best investments that suits their needs and expected return.

Target Market(s)

financial institutions, Corporates, high-net worth individuals

Industry/Entity Type

Financial Service

Contact Information for Business Card

Font styles to use
Other font styles liked:
• applemyungjo

Colors
00a990
848484

Requirements
Must have
• the logo at the back
Nice to have
• Finesse
Should not have
• boldness

```html
<!DOCTYPE html>
<html lang="en">
<head>
<meta charset="utf-8">
<title>Quarrow Financial Services – Business Cards</title>
<link href="https://fonts.googleapis.com/css2?family=Lato:wght@300;400&display=swap" rel="stylesheet">
<style>
  :root {
    --teal: #1fab93;
    --teal-dark: #00a990;
    --grey: #848484;
    --ink: #4a4a4a;
    --paper: #ffffff;
    --backdrop: #3d3d3d;
    --mark-tint: #d9dfd3;
  }
  * { box-sizing: border-box; margin: 0; padding: 0; }
  html, body { width: 1200px; height: 810px; overflow: hidden; }
  body {
    background: var(--backdrop);
    font-family: "Lato", Arial, sans-serif;
    position: relative;
  }
  .card {
    position: absolute;
    top: 250px;
    width: 540px;
    height: 310px;
    border-radius: 18px;
    overflow: hidden;
  }
  .card--front { left: 40px; background: var(--teal); color: var(--paper); }
  .card--back { left: 620px; background: var(--paper); color: var(--ink); }

  .brand {
    position: absolute;
    left: 0; right: 0;
    display: flex;
    flex-direction: column;
    align-items: center;
    font-weight: 300;
    text-transform: uppercase;
    letter-spacing: 0.16em;
  }
  .brand__square {
    width: 34px; height: 34px;
    margin-bottom: 12px;
  }
  .brand__name { font-size: 38px; line-height: 1; }
  .brand__sub { font-size: 11px; letter-spacing: 0.32em; margin-top: 6px; }

  .card--front .brand { top: 78px; }
  .card--front .brand__square { background: rgba(255,255,255,0.85); }
  .card--front .site {
    position: absolute;
    left: 0; right: 0; top: 232px;
    text-align: center;
    font-size: 15px;
    font-weight: 400;
    letter-spacing: 0.02em;
  }

  .card--back .brand { top: 24px; color: var(--ink); }
  .card--back .brand__square { width: 26px; height: 26px; margin-bottom: 8px; background: var(--mark-tint); }
  .card--back .brand__name { font-size: 28px; }
  .card--back .brand__sub { font-size: 9px; }

  .person {
    position: absolute;
    left: 200px; top: 140px;
    text-align: center;
    width: 140px;
  }
  .person__name { color: var(--teal-dark); font-size: 20px; font-weight: 400; }
  .person__role { color: var(--grey); font-size: 14px; font-weight: 300; margin-top: 2px; }

  .rule {
    position: absolute;
    height: 1.5px;
    background: var(--teal-dark);
  }
  .rule--upper { left: 330px; right: 0; top: 140px; }
  .rule--lower { left: 0; right: 0; top: 236px; }

  .address {
    position: absolute;
    right: 26px; top: 152px;
    text-align: right;
    color: var(--grey);
    font-size: 13px;
    font-weight: 300;
    line-height: 1.35;
  }

  .contacts {
    position: absolute;
    left: 26px; top: 248px;
    list-style: none;
    color: var(--ink);
    font-size: 13px;
    font-weight: 300;
    line-height: 1.45;
  }
  .contacts li { display: flex; align-items: center; gap: 8px; }
  .contacts svg { width: 11px; height: 11px; fill: var(--teal-dark); flex: none; }
</style>
</head>
<body>

  <section class="card card--front" aria-label="Card front">
    <div class="brand">
      <span class="brand__square"></span>
      <span class="brand__name">Quarrow</span>
      <span class="brand__sub">Financial Services</span>
    </div>
    <p class="site">www.quarrowfinancial.com</p>
  </section>

  <section class="card card--back" aria-label="Card back">
    <div class="brand">
      <span class="brand__square"></span>
      <span class="brand__name">Quarrow</span>
      <span class="brand__sub">Financial Services</span>
    </div>

    <div class="person">
      <p class="person__name">Daniel Hart</p>
      <p class="person__role">President</p>
    </div>

    <span class="rule rule--upper"></span>

    <address class="address">
      Suite 210, Estate 8/4<br>
      Po.Box No 51380<br>
      Country code USA
    </address>

    <span class="rule rule--lower"></span>

    <ul class="contacts">
      <li>
        <svg viewBox="0 0 24 24" aria-hidden="true"><path d="M6.6 10.8a15.5 15.5 0 0 0 6.6 6.6l2.2-2.2a1 1 0 0 1 1-.25 11.4 11.4 0 0 0 3.6.57 1 1 0 0 1 1 1V20a1 1 0 0 1-1 1A17 17 0 0 1 3 4a1 1 0 0 1 1-1h3.5a1 1 0 0 1 1 1c0 1.25.2 2.45.57 3.6a1 1 0 0 1-.25 1z"/></svg>
        (000) 0000 0000
      </li>
      <li>
        <svg viewBox="0 0 24 24" aria-hidden="true"><path d="M2 5h20v14H2zm2 2v.5l8 5 8-5V7z"/></svg>
        info@quarrowfinancial.com
      </li>
      <li>
        <svg viewBox="0 0 24 24" aria-hidden="true"><circle cx="12" cy="12" r="10"/></svg>
        www.quarrowfinancial.com
      </li>
    </ul>
  </section>

</body>
</html>
```